Surgical Sales Presentation Folder

Presentation folder; three panel; custom cutouts; Six 8.5 x 11 full color sales sheets to be bound into presentation folder; 5 full color sales sheets, stepped, longest being 8.5 x 11.
We are Brantley Surgical Group and we are a surgical company that supports physicians who wish to become surgeons. Our clients are Physicians. As such, the design needs to be very professional.
I have included a list of photos and a letter describing what we like about each photo. I have included the verbiage with page identifiers. If this makes scene, please feel free to add photos to the inside of the folder or I can provide you with examples that we think are similar to what we are looking for.
Updates
Target Market(s)
Doctors who want to be surgeons.
Industry/Entity Type
Sales
Requirements
Must have
- Presentation folder; three panel; custom cutouts; Six 8.5 x 11 full color sales sheets to be bound into presentation folder; 5 full color sales sheets, stepped, longest being 8.5 x 11.

```html
<!DOCTYPE html>
<html lang="en">
<head>
<meta charset="utf-8">
<title>Medical Practice vs. Surgical Practice — Brantley Surgical Group</title>
<link rel="stylesheet" href="https://fonts.googleapis.com/css2?family=Arimo:wght@400;700&family=Roboto+Condensed:wght@400&display=swap">
<style>
  :root {
    --sky: #5eb1e6;
    --band: #78c1f0;
    --rule: #8cc8ee;
    --navy: #1d4a78;
    --ink: #2a2a2a;
    --paper: #ffffff;
  }
  html, body {
    margin: 0;
    padding: 0;
    overflow: hidden;
    background: var(--paper);
  }
  .sheet {
    position: relative;
    width: 856px;
    height: 1200px;
    background: var(--paper);
    overflow: hidden;
  }
  .brand {
    position: absolute;
    top: 42px;
    right: 40px;
    display: flex;
    align-items: center;
    gap: 9px;
  }
  .brand-dot {
    width: 34px;
    height: 34px;
    border-radius: 50%;
    background: var(--navy);
  }
  .brand-name {
    font-family: "Arimo", Arial, sans-serif;
    font-weight: 700;
    font-size: 19px;
    color: var(--navy);
    letter-spacing: 0.2px;
  }
  .sheet-title {
    position: absolute;
    top: 116px;
    left: 0;
    width: 100%;
    margin: 0;
    text-align: center;
    font-family: "Arimo", Arial, sans-serif;
    font-weight: 700;
    font-size: 24px;
    color: var(--sky);
    letter-spacing: 0.2px;
  }
  .rule {
    position: absolute;
    left: 112px;
    width: 634px;
    height: 0;
    border-top: 1.5px solid var(--rule);
  }
  .rule-top { top: 186px; }
  .rule-bottom { top: 662px; }
  .content {
    position: absolute;
    top: 220px;
    left: 113px;
    width: 634px;
    font-family: "Roboto Condensed", "Arial Narrow", sans-serif;
    font-size: 14.3px;
    line-height: 19px;
    color: var(--ink);
  }
  .content p {
    margin: 0 0 2px;
  }
  .content .item {
    text-indent: 6px;
  }
  .content .bullet {
    padding-left: 6px;
  }
  .content .gap {
    margin-top: 16px;
  }
  .footer-band {
    position: absolute;
    left: 0;
    bottom: 0;
    width: 100%;
    height: 52px;
    background: var(--band);
  }
</style>
</head>
<body>
<div class="sheet">
  <header class="brand">
    <span class="brand-dot"></span>
    <span class="brand-name">Brantley Surgical Group</span>
  </header>

  <h1 class="sheet-title">MEDICAL PRACTICE VS. SURGICAL PRACTICE</h1>
  <div class="rule rule-top"></div>

  <section class="content">
    <p>Clinicore/HealthView conducted a survey of 24,000 physicians representing 25 different medical specialties. They found that:</p>
    <p class="item">Only 54% of the physicians said they would choose medicine again as a career, down from 69% only three years ago.</p>
    <p class="item">Just 41% would choose the same specialty again.</p>
    <p class="item">Only 25% of doctors said they would choose the same practice setting, compared with 50% two years ago.</p>
    <p class="item">This same article identifies, &nbsp;frustration and discontent among physicians &nbsp;due to:</p>
    <p class="bullet">o Declining incomes</p>
    <p class="bullet">o Excessive paperwork</p>
    <p class="bullet">o Vast uncertainty about changes dictated by the Affordable Care Act</p>

    <p class="gap">When we look specifically at surgeons, the Surgical Practice Review found that with respect to career satisfaction:</p>
    <p class="item">71 % of the study participants indicated that they would become a physician again.</p>
    <p class="item">74% would become a surgeon again, if they could revisit their specialty choice.</p>
    <p class="item">And they included Plastic Surgeons in the specialties with the greatest satisfaction with overall career choice.</p>

    <p class="gap">In fact, according to an article in Market Daily News, the highest paying profession last year was Surgery!</p>
  </section>

  <div class="rule rule-bottom"></div>
  <footer class="footer-band"></footer>
</div>
</body>
</html>
```